FIXOR DENTAIRE LILAS box for dental resine pink to repair dentures broken

I will need a design for a box of pink dental resin. It is a pink dental resin which is intended for sale to individuals on Velmora to repair or make small touch-ups or modifications to their dental prostheses. The title FIXOR DENTAIRE LILAS must be clearly visible as well as the company logo. .I leave it to your creative mind to make an attractive and highly impactful and clearly visible sales design.
It is also necessary to make it clear to buyers through text or a vector image the purpose of the product: to repair a dental prosthesis.
Updates
Faible participation designers
Target Market(s)
Particulars who have need to repair their dentures
Look and feel
Each slider illustrates characteristics of the customer's brand and the style your logo design should communicate.

```html
<!DOCTYPE html>
<html lang="fr">
<head>
<meta charset="utf-8">
<title>Fixor Dentaire Lilas – Laboratoire Orvanel</title>
<link href="https://fonts.googleapis.com/css2?family=Alfa+Slab+One&family=Barlow+Condensed:wght@400;500&family=Montserrat:wght@600&display=swap" rel="stylesheet">
<style>
  :root {
    --magenta: #d81b5b;
    --green: #55a85c;
    --logo-green: #6aab2e;
    --top-white: #f6f6f6;
    --pink-panel: #f3e0e4;
    --pink-halo: #f1d9df;
    --tooth-white: #f4f4f4;
    --ink: #1a1a1a;
  }
  html, body { margin: 0; padding: 0; overflow: hidden; }
  body { width: 1154px; height: 1200px; background: var(--pink-panel); }
  .box {
    position: relative; width: 1154px; height: 1200px; overflow: hidden;
    background: linear-gradient(to bottom, var(--top-white) 0 512px, var(--pink-panel) 512px 100%);
  }
  .brand {
    position: absolute; top: 78px; left: 213px; height: 150px;
    display: flex; align-items: center; gap: 26px;
    font-family: "Montserrat", sans-serif; font-weight: 600; color: var(--logo-green);
  }
  .brand-square { width: 140px; height: 140px; background: var(--logo-green); flex: none; }
  .brand-name { font-size: 56px; line-height: 1.08; letter-spacing: 3px; }
  .brand-name .since { display: block; font-size: 26px; letter-spacing: 1px; margin-top: 4px; }
  .artwork { position: absolute; inset: 0; width: 1154px; height: 1200px; }
  .title-word { font-family: "Alfa Slab One", serif; font-size: 96px; fill: var(--magenta); }
  .product-word {
    font-family: "Alfa Slab One", serif; font-size: 196px; fill: #ffffff;
    stroke: var(--magenta); stroke-width: 4; paint-order: stroke;
  }
  .purpose-text { font-family: "Barlow Condensed", sans-serif; font-weight: 500; font-size: 56px; fill: var(--ink); }
  .volume { font-family: "Barlow Condensed", sans-serif; font-weight: 400; font-size: 42px; fill: var(--ink); }
</style>
</head>
<body>
<main class="box">
  <header class="brand">
    <span class="brand-square"></span>
    <div class="brand-name">LABORATOIRE<br>ORVANEL<span class="since">Depuis 1990</span></div>
  </header>

  <svg class="artwork" viewBox="0 0 1154 1200">
    <path id="title-curve" d="M240 440 Q577 300 914 440" fill="none"/>
    <text class="title-word" text-anchor="middle"><textPath href="#title-curve" startOffset="50%" textLength="660" lengthAdjust="spacingAndGlyphs">Fixor Lilas</textPath></text>

    <rect class="band" x="0" y="528" width="1154" height="111" fill="var(--magenta)"/>

    <g class="mouth" role="img" aria-label="Illustration d'une bouche ouverte aux dents blanches et gencives vertes">
      <ellipse cx="577" cy="580" rx="368" ry="196" fill="var(--pink-halo)"/>
      <ellipse cx="577" cy="580" rx="352" ry="180" fill="var(--tooth-white)" stroke="var(--green)" stroke-width="14"/>
      <ellipse cx="577" cy="585" rx="326" ry="112" fill="var(--magenta)"/>
    </g>

    <text class="product-word" x="577" y="655" text-anchor="middle" textLength="630" lengthAdjust="spacingAndGlyphs">DENTAIRE</text>

    <g class="tooth before" role="img" aria-label="Dent abîmée">
      <path d="M175 880 C175 845 205 835 233 850 C261 835 291 845 291 880 C291 915 280 930 275 960 L258 960 L248 918 L218 918 L208 960 L191 960 C186 930 175 915 175 880 Z" fill="#fff" stroke="var(--ink)" stroke-width="6" stroke-linejoin="round"/>
    </g>
    <text class="purpose-text" x="562" y="879" text-anchor="middle" textLength="380" lengthAdjust="spacingAndGlyphs">Pour la réparation</text>
    <rect x="327" y="898" width="475" height="11" fill="var(--magenta)"/>
    <polygon points="795,884 835,903.5 795,923" fill="var(--magenta)"/>
    <text class="purpose-text" x="568" y="972" text-anchor="middle" textLength="492" lengthAdjust="spacingAndGlyphs">de prothèses dentaires</text>
    <g class="tooth after" role="img" aria-label="Dent réparée">
      <path d="M858 880 C858 845 888 835 916 850 C944 835 974 845 974 880 C974 915 963 930 958 960 L941 960 L931 918 L901 918 L891 960 L874 960 C869 930 858 915 858 880 Z" fill="#fff" stroke="var(--ink)" stroke-width="6" stroke-linejoin="round"/>
    </g>

    <text class="volume" x="577" y="1157" text-anchor="middle">100ml</text>
  </svg>
</main>
</body>
</html>
```